Talbern Learning Recruitment Business Cards

We need business cards designed for our growing recruitment business.
We have just launched our offices in Sydney Melbourne and have a well established business in Perth. We are a fun young firm that specialise in Early Years Education Recruitment.
Our vision mission values are below
Our Vision:
To be:
the single, nationally recognised leader in the Early Childhood Sector.
a multifaceted organisation with a network of expertly driven facilities in the Early Childhood Sector, acknowledged as an organisation of integrity, innovation, heart and community.

Our Mission:
To provide superior quality recruitment services and solutions to the Early Childhood sector.
We empower our candidates to succeed.
We engage in trusted partnerships with our clients.
We grow our business/network/community, with passion and integrity.

Our Values:

We… are REAL
think: CUSTOMER
find: SOLUTIONS
achieve: RESULTS
enjoy: WHAT WE DO

Our website is www.talbernlearning.com feel free to visit it for inspiration.
Name Felix Ormsby
Title National Director
1300 057 812
0462 315 706
felix@talbernstaffing.com
website www.talbernlearning.com

I have attached our current business cards and logo designs to view

Target Market(s)

Recruitment

Industry/Entity Type

Business

Contact Information for Business Card

Name Felix Ormsby
Title National Director
1300 057 812
0462 315 706

Font styles to use
Serif

Requirements
Must have
• Company Values and the cities we have offices in Perth | Sydney | Melbourne
Nice to have
• Our Vision on the card
• Our Vision:
• To be a nationally recognised leader in the Early Childhood Sector.
• A multifaceted organisation with a network of expertly driven facilities in the Early Childhood Sector, acknowledged as an organisation of integrity, innovation, heart and community.

```html
<!DOCTYPE html>
<html lang="en">
<head>
<meta charset="utf-8">
<title>Talbern Learning Recruitment – Business Cards</title>
<link href="https://fonts.googleapis.com/css2?family=Lora:wght@400;500&display=swap" rel="stylesheet">
<style>
  :root {
    --backdrop: #e9ecf0;
    --navy-deep: #0c2548;
    --navy: #1a4478;
    --navy-light: #2f5f96;
    --sky: #2b8fce;
    --ink-blue: #1f5f96;
    --white: #ffffff;
    --soft-white: rgba(255,255,255,0.88);
    --rule: rgba(255,255,255,0.45);
  }
  * { margin: 0; padding: 0; box-sizing: border-box; }
  html, body { width: 1200px; height: 894px; overflow: hidden; }
  body {
    background: var(--backdrop);
    font-family: "Lora", serif;
    position: relative;
  }
  .card {
    position: absolute;
    width: 560px;
    height: 342px;
    border-radius: 4px;
    overflow: hidden;
    box-shadow: 0 10px 28px rgba(12,37,72,0.22);
  }

  /* Front */
  .card-front {
    left: 50px; top: 80px;
    background: linear-gradient(160deg, var(--navy-light) 0%, var(--navy) 45%, var(--navy-deep) 100%);
  }
  .front-header {
    position: absolute; left: 0; top: 0; width: 100%; height: 138px;
    background: var(--white);
  }
  .brand {
    position: absolute; left: 34px; top: 40px;
    display: flex; align-items: center; gap: 14px;
  }
  .brand-disc {
    width: 70px; height: 70px; border-radius: 50%;
    border: 4px solid var(--sky);
    flex: none;
  }
  .brand-name {
    font-size: 21px; font-weight: 400; letter-spacing: 1px;
    color: var(--ink-blue); line-height: 1.1;
  }
  .brand-tagline {
    font-size: 11.5px; font-weight: 400; color: var(--sky);
    margin-top: 5px;
  }
  .contact {
    position: absolute; left: 34px; top: 164px; width: 300px;
    color: var(--white);
  }
  .contact-name { font-size: 20px; font-weight: 400; line-height: 1.2; }
  .contact-title { font-size: 12px; color: var(--soft-white); margin-bottom: 8px; }
  .contact-line {
    font-size: 12.5px; color: var(--soft-white); letter-spacing: 0.2px;
    padding: 5px 0; border-top: 1px solid var(--rule);
  }

  /* Back */
  .card-back {
    left: 590px; top: 470px;
    background: linear-gradient(160deg, var(--navy-light) 0%, var(--navy) 50%, var(--navy-deep) 100%);
  }
  .gloss-band {
    position: absolute; left: 0; top: 0; width: 100%; height: 100%;
  }
  .values {
    position: absolute; right: 30px; top: 32px;
    text-align: right; color: var(--soft-white);
    font-size: 14px; line-height: 1.5; letter-spacing: 0.2px;
  }
  .back-brand {
    position: absolute; left: 40px; top: 196px;
    display: flex; align-items: center; gap: 12px;
  }
  .back-brand .brand-disc { width: 62px; height: 62px; }
  .back-brand .brand-name { font-size: 17px; }
  .offices {
    position: absolute; right: 30px; bottom: 22px;
    color: var(--soft-white);
    font-size: 12.5px; letter-spacing: 1px;
  }
</style>
</head>
<body>

  <section class="card card-front" aria-label="Business card front">
    <div class="front-header"></div>
    <div class="brand">
      <div class="brand-disc"></div>
      <div>
        <div class="brand-name">TALBERN LEARNING</div>
        <div class="brand-tagline">Bringing quality to education recruitment</div>
      </div>
    </div>
    <div class="contact">
      <div class="contact-name">Felix Ormsby</div>
      <div class="contact-title">National Director</div>
      <div class="contact-line">1300 057 812</div>
      <div class="contact-line">0462 315 706</div>
      <div class="contact-line">felix@talbernstaffing.com</div>
      <div class="contact-line">www.talbernlearning.com</div>
    </div>
  </section>

  <section class="card card-back" aria-label="Business card back">
    <svg class="gloss-band" viewBox="0 0 560 342" preserveAspectRatio="none" aria-hidden="true">
      <defs>
        <linearGradient id="band" x1="0" y1="0" x2="1" y2="0">
          <stop offset="0" stop-color="#ffffff" stop-opacity="0.95"/>
          <stop offset="0.45" stop-color="#dfe8f2" stop-opacity="0.75"/>
          <stop offset="1" stop-color="#ffffff" stop-opacity="0.08"/>
        </linearGradient>
      </defs>
      <polygon points="0,196 560,98 560,176 0,300" fill="url(#band)"/>
    </svg>
    <div class="values">
      We… are REAL<br>
      think: CUSTOMER<br>
      find: SOLUTIONS<br>
      achieve: RESULTS<br>
      enjoy: WHAT WE DO
    </div>
    <div class="back-brand">
      <div class="brand-disc"></div>
      <div class="brand-name">TALBERN LEARNING</div>
    </div>
    <div class="offices">Perth | Sydney | Melbourne</div>
  </section>

</body>
</html>
```